BRIGHT HEARTH - A5 flyer design

Please see updated brief attached

We need an engaging A5 flyer to accompany a targeted mail out to help recruit households to our BRIGHT HEARTH project

Warmwell Aid is a small environmental small charity based in NW London. We work to improve the health and well being of vulnerable people and communities living in fuel poverty. Through educating, advising and supporting, we provide practical solutions that enable people to live in warm, dry and comfortable homes, in control of their fuel use and their fuel costs.

We have recently been awarded a grant to run a project to conduct in home trials to test two new and innovative energy saving measures. The project is called BRIGHT HEARTH.

Aim of Flyer: to immediately engage households in want to partake in the project. It will be accompanied with a letter giving more in depth details about the project, criteria for participating etc so the flyer will not need to carry all the detail

Target Audience: Households in fuel poverty predominately from the social housing sector, low income, ethnically diverse and may have vulnerable household members (e.g. long term health conditions, debts, elderly etc)

More details in full brief attached.
Contact: dan@warmwellaid.org.uk or 020 7946 0718

Target Market(s)

low income households in fuel poverty - NW London area

Requirements
Must have
• Project name
• Company logo/s
Nice to have
• highlight how the project can save people money/energy
• Free to participate in project
• highlight the chance to win prizes for partaking

```html
<!DOCTYPE html>
<html lang="en">
<head>
<meta charset="utf-8">
<title>BRIGHT HEARTH – Flyer</title>
<link rel="stylesheet" href="https://fonts.googleapis.com/css2?family=Arimo:ital@0;1&family=Black+Ops+One&display=swap">
<style>
  :root {
    --kraft-light: #d2b088;
    --kraft-mid: #c29d71;
    --kraft-dark: #a57e57;
    --ink: #2f1d0e;
    --torn-dark: #2a1a0d;
    --torn-edge: #e8d3b4;
    --band-text: #e8d3b4;
  }
  html, body {
    margin: 0;
    padding: 0;
    overflow: hidden;
    background: #ffffff;
  }
  .flyer {
    position: relative;
    width: 847px;
    height: 1200px;
    overflow: hidden;
    background:
      radial-gradient(ellipse at 30% 40%, var(--kraft-light) 0%, transparent 60%),
      radial-gradient(ellipse at 80% 85%, var(--kraft-dark) 0%, transparent 55%),
      linear-gradient(170deg, var(--kraft-mid), var(--kraft-light) 45%, var(--kraft-mid));
    color: var(--ink);
    font-family: "Arimo", Arial, sans-serif;
  }
  .torn-edge {
    position: absolute;
    top: 0;
    left: 0;
    width: 847px;
    height: 70px;
  }
  .masthead {
    position: absolute;
    top: 8px;
    left: 76px;
    width: 706px;
    display: flex;
    justify-content: space-between;
    align-items: center;
    font-family: "Black Ops One", Impact, sans-serif;
    font-size: 22px;
    color: var(--band-text);
    letter-spacing: 1px;
  }
  .org-name { display: flex; align-items: center; gap: 8px; }
  .org-dot { width: 12px; height: 12px; border-radius: 50%; background: var(--band-text); }
  .block {
    position: absolute;
    left: 76px;
    width: 716px;
    margin: 0;
    font-size: 23.5px;
    line-height: 34px;
    hyphens: auto;
  }
  .label {
    font-family: "Black Ops One", Impact, sans-serif;
    font-size: 25px;
    font-variant: small-caps;
  }
  .technologies { top: 72px; }
  .wattly { top: 226px; }
  .heatnest { top: 452px; }
  .criteria-block { top: 676px; }
  .heading {
    font-family: "Black Ops One", Impact, sans-serif;
    font-variant: small-caps;
    font-size: 26px;
    font-weight: normal;
    margin: 0;
    line-height: 34px;
  }
  .criteria {
    list-style: none;
    margin: 0;
    padding: 0;
    font-style: italic;
  }
  .limit {
    top: 980px;
    font-family: "Black Ops One", Impact, sans-serif;
    font-variant: small-caps;
    font-size: 26px;
  }
  .contact {
    top: 1040px;
    font-family: "Black Ops One", Impact, sans-serif;
    font-size: 24px;
    line-height: 34px;
  }
  .contact p { margin: 0; }
  .contact .caps { font-variant: small-caps; }
</style>
</head>
<body>
<div class="flyer">
  <svg class="torn-edge" viewBox="0 0 847 70" aria-hidden="true">
    <polygon fill="var(--torn-edge)" points="0,0 847,0 847,52 820,60 800,48 776,62 750,50 722,66 700,52 676,60 650,46 624,64 600,52 572,62 548,48 522,66 498,54 470,62 446,48 420,64 396,52 370,60 344,46 320,64 294,52 270,62 244,48 220,66 194,54 168,62 142,48 118,64 92,52 66,62 40,48 18,60 0,52"/>
    <polygon fill="var(--torn-dark)" points="0,0 847,0 847,44 822,52 802,40 776,54 752,42 724,58 700,44 676,52 650,38 626,56 600,44 574,54 548,40 524,58 498,46 472,54 446,40 420,56 396,44 370,52 346,38 320,56 296,44 270,54 246,40 220,58 196,46 170,54 144,40 118,56 94,44 66,54 42,40 18,52 0,44"/>
  </svg>

  <header class="masthead">
    <span class="project-name">BRIGHT HEARTH</span>
    <span class="org-name"><span class="org-dot"></span>Warmwell Aid</span>
  </header>

  <p class="block technologies"><span class="label">Technologies:</span> One technology helps to reduce electricity consumption, the other gas consumption. The two new energy saving measures that we will be trailing will potentially reduce energy costs by up to 40%</p>

  <p class="block wattly"><span class="label">WATTLY@</span> is a smart electricity monitoring device providing the user with real time energy consumption data at appliance level. It allows users to access information about their electricity usage at any time. It shows householders where they can make savings and reduce their electricity bill through simple changes to their daily routine.</p>

  <p class="block heatnest"><span class="label">HeatNest TRV</span> is a thermostatic radiator valve and monitoring package, which provides room by room heating control. The on board intelligence learns the usage pattern of the room and automatically adjusts the temperature to save energy and money! It also monitors humidity to ensure rooms have a healthy living environment.</p>

  <section class="block criteria-block">
    <h2 class="heading">Criteria for Participation</h2>
    <ol class="criteria">
      <li>1. Currently have a working gas central heating,&nbsp; and</li>
      <li>2. Have radiators with thermostatic controls, and</li>
      <li>3. Owner/occupier, private tenant or social housing resident</li>
      <li>4. Must have access to the internet/wifi (for automatic monitoring of the data)</li>
      <li>5. Willing to participate for the project duration (until April 2017)</li>
    </ol>
  </section>

  <p class="block limit">The service is limited to the first 60 households!</p>

  <div class="block contact">
    <p><span class="caps">Tel:</span> 020 7946 0142</p>
    <p><span class="caps">Toll-free:</span> 0808 157 0192</p>
    <p class="caps">hello@warmwellaid.org.uk</p>
  </div>
</div>
</body>
</html>
```